TalentHive web site

We need a new look for our web site TalentHive-software.example, we use a lot of keywords to maximize our organic searches as well as Searchly landing pages.

Our product TalentHive is a web based Saas applicant & recruiting solution, so with the "cloud" being one of the bid IT buzzes lately we want to leverage that.

We will want to have 3 options for companies a Basic, Professional & Enterprise, with a grid of feature offerings the buyer can choose from.

We also want a strong call to action to enroll in a free webinar.

Target Market(s)

HR and Recruiters for mid to large size employers. No market vertical

Requirements
Must have
• Strong graphics, we currently have some screen shots.

```html
<!DOCTYPE html>
<html lang="en">
<head>
<meta charset="utf-8">
<title>TalentHive</title>
<link rel="stylesheet" href="https://fonts.googleapis.com/css2?family=Crimson+Text:wght@400;600;700&family=Libre+Baskerville:wght@700&family=Open+Sans:wght@400;600;700&display=swap">
<style>
  :root {
    --navy-top: #16305a;
    --navy: #1f3c69;
    --navy-card: #1a3460;
    --navy-foot: #162d52;
    --nav-blue: #5f9dd8;
    --sky: #8db8e3;
    --sky-soft: #a9cbee;
    --button: #123a66;
    --white: #ffffff;
    --ink: #0d1f3a;
    --serif: "Crimson Text", Georgia, serif;
    --display: "Libre Baskerville", Georgia, serif;
    --sans: "Open Sans", Arial, sans-serif;
  }
  * { box-sizing: border-box; margin: 0; padding: 0; }
  html, body { width: 1200px; height: 2480px; overflow: hidden; }
  body { position: relative; background: var(--navy); font-family: var(--serif); color: var(--white); }
  .abs { position: absolute; }

  /* header */
  .top-band { left: 0; top: 0; width: 1200px; height: 143px; background: var(--navy-top); }
  .nav-bar { left: 0; top: 143px; width: 1200px; height: 83px; background: var(--nav-blue); }
  .nav-link { top: 177px; font-family: var(--sans); font-size: 15px; font-weight: 600; color: var(--white); letter-spacing: 0.3px; }
  .brand-box { left: 421px; top: 99px; width: 380px; height: 179px; background: var(--white); display: flex; align-items: center; justify-content: center; z-index: 2; }
  .brand-name { font-family: var(--sans); font-size: 66px; font-weight: 400; color: var(--ink); letter-spacing: -1px; }

  /* hero */
  .hero-photo { left: 0; top: 226px; width: 1200px; height: 412px;
    background: linear-gradient(100deg, #0e2a5c 0%, #1f4c8e 30%, #5d8fcf 55%, #a6c8ef 75%, #3e6fb0 100%); }
  .hero-title { left: 96px; top: 348px; font-family: var(--display); font-size: 108px; font-weight: 700; color: var(--white); letter-spacing: -1px; line-height: 1; }
  .hero-sub { left: 112px; top: 472px; font-family: var(--serif); font-size: 26px; font-weight: 700; color: var(--white); }

  /* plan columns */
  .plans { left: 0; top: 638px; width: 1200px; height: 402px; background: var(--sky); }
  .plan { top: 680px; width: 360px; text-align: center; color: var(--ink); }
  .plan h2 { font-family: var(--serif); font-size: 29px; font-weight: 700; margin-bottom: 22px; }
  .plan p { font-size: 22px; line-height: 24px; color: var(--white); }
  .plan .price { margin-top: 28px; }
  .plan-divider { top: 688px; width: 2px; height: 261px; background: var(--navy); }
  .pill { height: 58px; border-radius: 8px; background: var(--button); color: var(--white); font-size: 22px; display: flex; align-items: center; justify-content: center; }
  .plan .pill { margin: 28px auto 0; width: 286px; }
  .section-fade { left: 0; top: 1040px; width: 1200px; height: 22px; background: linear-gradient(#8db8e3, #1f3c69); }

  /* feature grid */
  .webinar-button { left: 842px; top: 1134px; width: 286px; height: 49px; border-radius: 7px; background: var(--white); color: var(--navy); font-size: 22px; font-weight: 700; display: flex; align-items: center; justify-content: center; }
  .feature-row { left: 74px; width: 1054px; background: var(--navy-card); border-radius: 4px; }
  .feature-row p { position: absolute; top: 56px; width: 400px; font-size: 25px; line-height: 27px; color: var(--white); }
  .feature-row .col-left { left: 77px; }
  .feature-row .col-right { left: 597px; }

  /* summary */
  .summary { top: 2012px; width: 460px; text-align: center; }
  .summary h2 { font-size: 29px; font-weight: 700; color: var(--sky-soft); margin-bottom: 14px; }
  .summary p { font-size: 21px; line-height: 24px; color: var(--white); padding: 0 50px; }
  .summary-divider { left: 635px; top: 1976px; width: 2px; height: 184px; background: #7d9cc4; }

  /* footer */
  .footer { left: 0; top: 2230px; width: 1200px; height: 250px; background: var(--navy-foot); }
  .foot-col { top: 2270px; }
  .foot-col h3 { font-size: 24px; font-weight: 400; color: var(--sky-soft); line-height: 28px; }
  .foot-col li { list-style: none; font-size: 19px; line-height: 30px; color: var(--white); }
  .foot-rule { left: 157px; top: 2427px; width: 883px; border-top: 2px dotted #4d6d96; }
  .copyright { left: 0; top: 2436px; width: 1200px; text-align: center; font-family: var(--sans); font-size: 15px; font-weight: 700; color: var(--white); }
</style>
</head>
<body>
  <header>
    <div class="abs top-band"></div>
    <nav class="abs nav-bar" aria-label="Main"></nav>
    <span class="abs nav-link" style="left:110px">HOME</span>
    <span class="abs nav-link" style="left:192px">PLANS</span>
    <span class="abs nav-link" style="left:270px">FEATURES</span>
    <span class="abs nav-link" style="left:846px">WEBINAR</span>
    <span class="abs nav-link" style="left:948px">CLOUD</span>
    <span class="abs nav-link" style="left:1030px">CONTACT</span>
    <div class="abs brand-box"><span class="brand-name">TalentHive</span></div>
  </header>

  <section>
    <div class="abs hero-photo" role="img" aria-label="Upward view of glass office towers against a blue sky"></div>
    <h1 class="abs hero-title">Hire faster</h1>
    <p class="abs hero-sub">Applicant tracking and recruiting, all in the cloud</p>
  </section>

  <section>
    <div class="abs plans"></div>
    <div class="abs plan" style="left:37px">
      <h2>Basic</h2>
      <p>Post jobs and track<br>applicants online.<br>Up to 5 recruiters.</p>
      <p class="price">From $49 a month</p>
      <div class="pill">Choose Basic</div>
    </div>
    <div class="abs plan-divider" style="left:409px"></div>
    <div class="abs plan" style="left:420px">
      <h2>Professional</h2>
      <p>Team workflows and<br>interview scheduling.<br>Up to 25 recruiters.</p>
      <p class="price">From $149 a month</p>
      <div class="pill">Choose Professional</div>
    </div>
    <div class="abs plan-divider" style="left:794px"></div>
    <div class="abs plan" style="left:805px">
      <h2>Enterprise</h2>
      <p>Custom roles, reports<br>and integrations.<br>Unlimited recruiters.</p>
      <p class="price">Priced per company</p>
      <div class="pill">Talk to sales</div>
    </div>
    <div class="abs section-fade"></div>
  </section>

  <section>
    <div class="abs webinar-button">Join a free webinar</div>
    <div class="abs feature-row" style="top:1205px;height:171px">
      <p class="col-left">Job posting: publish openings<br>to many boards. All plans.</p>
      <p class="col-right">Applicant tracking: follow every<br>candidate stage. All plans.</p>
    </div>
    <div class="abs feature-row" style="top:1390px;height:165px">
      <p class="col-left">Career site: a branded page<br>for your jobs. All plans.</p>
      <p class="col-right">Resume search: find talent by<br>skills and keywords. All plans.</p>
    </div>
    <div class="abs feature-row" style="top:1569px;height:168px">
      <p class="col-left">Interview scheduling: book<br>panels fast. Professional+.</p>
      <p class="col-right">Team reviews: share scorecards<br>with managers. Professional+.</p>
    </div>
    <div class="abs feature-row" style="top:1750px;height:168px">
      <p class="col-left">Custom reports: measure time<br>to hire. Enterprise only.</p>
      <p class="col-right">HR integrations: connect your<br>payroll and HRIS. Enterprise only.</p>
    </div>
  </section>

  <section>
    <div class="abs summary" style="left:106px">
      <h2>Free webinar</h2>
      <p>See TalentHive live and enroll in our weekly free demo.</p>
    </div>
    <div class="abs summary-divider"></div>
    <div class="abs summary" style="left:670px">
      <h2>Cloud ready</h2>
      <p>No installs: recruit from any browser, anywhere.</p>
    </div>
  </section>

  <footer>
    <div class="abs footer"></div>
    <div class="abs foot-col" style="left:121px">
      <h3>TalentHive</h3>
      <ul><li>Meridian St</li><li>Harborview, Northland</li><li>TalentHive-software.example</li><li>+000-5550-0141</li></ul>
    </div>
    <div class="abs foot-col" style="left:402px">
      <h3>Support</h3>
      <ul><li>M-F 7am-9pm</li><li>Sat/Sun 6am-10pm</li></ul>
    </div>
    <div class="abs foot-col" style="left:592px">
      <h3>Plans</h3>
      <ul><li>Basic</li><li>Professional</li><li>Enterprise</li><li>Compare</li></ul>
    </div>
    <div class="abs foot-col" style="left:763px">
      <h3>Product</h3>
      <ul><li>Features</li><li>Cloud</li><li>Security</li><li>Webinars</li></ul>
    </div>
    <div class="abs foot-col" style="left:932px">
      <h3>Account</h3>
      <ul><li>Sign In</li><li>Free Trial</li><li>Contact Sales</li></ul>
    </div>
    <div class="abs foot-rule"></div>
    <p class="abs copyright">Copyright 2013 TalentHive</p>
  </footer>
</body>
</html>
```